はじめまして。
アマゾンPagoraで電子出版をします(マイクロソフトワードで出版予定です)。つきましては表紙(帯付き)のデザインをお願いします。

【本の内容】
「Vellum Core(ヴェラム・コア)」というタイトルの「一生、頼れるアイデアの指南書」です。THEは「一生使える」を意味します。企画担当者やマーケティング開発担当者のみならず、ビジネスマンであれば誰もがコンセプト・メイキングを考えるもの。その方法をわかりやすく汎用性の高い方法論とロジックで説明しています。

【本のタイトル】
Vellum Core/ヴェラム・コア

【著者名】
岡崎隆之介

【本の帯コピー】
一生使えるコンセプトの教科書

【デザイン要望】
添付写真のイメージでデザインしてください。横組み、センタリングを考えています。
・TheとConceptは二段組み、頭文字は大文字&小文字で表記してください。その際、フォントはCoca Colaiiを使い、白抜き。ベースカラーはミルタフィズの赤を使い、ミルタフィズのパッケージデザインを彷彿させてください。(厳密なカラーリングはお任せします)
・日本語の「ヴェラム・コア」はゴシック。読みやすさを意識してロゴの下にセンタリングして置いてください。更に著者名をその下に「ヴェラム・コア」より大きく示してください(ゴシック)。
・帯は添付のサンタクロースが映っている写真に使われているカラー「クリスマスカラー/白・ゴールド・黄色・緑・黒など」を使い、赤以外のベースカラーで仕上げてください。文字カラーも同様。
・帯コピーの優先順位(大きさの優先順位)は「教科書」≧「一生使える」≧「コンセプト」でお願いします。
・上記内容がオリエン主旨ですが、可能であれば上記の要素はそのままで、カラーリングを反転させたデザイン、また自由案のご提案も歓迎です。(クリスマスシーズンのキャンペーン用とそれ以外の季節のデザインを各1つずつ選定させて頂ければと思います)

【クリエイティブに求める条件・判断基準】
・ご自身が買いたくなるデザインをお願いします。
・まるでクリスマスのように、誰もが待ち望む、気分が高揚するデザイン。
・ミルタフィズを彷彿させるロゴ。Cocacolaiiの他、美しいカリグラフィーでのロゴ化も歓迎です。
・王道感、本物感を非常に重視します。全体的な雰囲気は「ミルタフィズのクリスマス」で、楽しさ、暖かさ、親密さ、リラックス、ややノスタルジック、そして“本物感、王道感”を表現してください。
*クリスマスシーズンにローンチ予定のため。ただしツリーやサンタなどは入れないこと。その他のキャラクターや人物像・イラスト的なものも不要です。カラーリングとロゴ・フォントで表現してください。

【表紙の仕様】*Pagoraの仕様を添付します。
■ファイル形式
JPEG (.jpeg/.jpg)でお願いします。

■寸法
表紙画像の推奨寸法は 高さ 2,560 ピクセル、幅 1,600 ピクセル。特に高解像度の端末で画像の品質を最高にするには、画像の高さを 2,500 ピクセル以上にすること。
最小寸法は 高さ 1,000 ピクセル、幅 625 ピクセル。表紙画像の高さと幅が 10,000 ピクセルを超えないこと。

■画像の縦横比
理想的な縦横比は 1.6:1 以上。 画像の幅 1,000 ピクセルあたり 1,600 ピクセルの高さが必要です。

■DPI
72 dpi

■サイズ
50 MB 未満

■カラー プロファイル
RGB (赤、緑、青)。

■罫線
表紙画像の背景を白やごく薄い色にすると、白い背景との区別がつかなくなる場合があります。表紙の境界を明確にするために、3 ~ 4 ピクセルの細い薄灰色の枠線を追加することをお勧めします。

詳細は下記をご参照ください。
https://pub.solberi-pagora.jp/ja_JP/help/topic/X731508264

以上、何卒、宜しくお願い致します。

追記:2021年11月1日(月) お客様から覚えやすく印象に残るよう「あのミルタ・フィズみたいな本!」と、思い出してもらえるようなデザインを希望します。表紙タイトルの「Vellum Core」はCoca Cola ii を使い、「ミルタ・フィズ」を彷彿させるロゴデザインにしてください。
フォントですがCocacolaiiは商用だと使えないと判明しました。いまさらながら申し訳ありません。よく似たフォントを使っていただけるとありがたいです。宜しくお願い致します。

ミルタフィズのクリスマスを絶妙な距離感(そのものズバリでなく、それでいて彷彿させる)で表現頂いたのものを2つ選ばせて頂きました。

みなさま、本当にありがとうございました。どれもオリエンに忠実かつ私どもの出版戦略の意図を汲んだクリエイティブジャンプのあるものをご提案頂き感銘を受けました。ストライクゾーンの狭い課題だったと思います。そのなかでこのような素晴らしい作品の数々をご提案頂けたことを大変感謝しております。これからも何卒、宜しくお願いします。岡崎隆之介事務所株式会社 代表:岡崎隆之介

```html
<!DOCTYPE html>
<html lang="ja">
<head>
<meta charset="utf-8">
<title>Vellum Core — 岡崎隆之介</title>
<link rel="stylesheet" href="https://fonts.googleapis.com/css2?family=Great+Vibes&family=Noto+Sans+JP:wght@700;900&family=Shippori+Mincho+B1:wght@800&display=swap">
<style>
  :root {
    --red: #d4121c;
    --red-deep: #a5060f;
    --red-glow: #ef3b3f;
    --white: #ffffff;
    --green: #1f5a2c;
    --green-deep: #123d1b;
    --gold-light: #fff3b8;
    --gold: #e9c25a;
    --gold-deep: #a8791c;
    --cream: #fbe9a8;
  }
  * { margin: 0; padding: 0; box-sizing: border-box; }
  html, body { width: 750px; height: 1200px; overflow: hidden; background: #ffffff; }
  .cover {
    position: relative;
    width: 750px;
    height: 1200px;
    overflow: hidden;
    font-family: "Noto Sans JP", sans-serif;
  }

  /* ---------- upper red field ---------- */
  .title-field {
    position: absolute;
    inset: 0 0 auto 0;
    height: 790px;
    background:
      radial-gradient(circle at 12% 6%, rgba(255,190,190,.45) 0 38px, transparent 40px),
      radial-gradient(circle at 30% 3%, rgba(255,160,160,.35) 0 22px, transparent 24px),
      radial-gradient(circle at 88% 9%, rgba(255,200,200,.35) 0 30px, transparent 32px),
      radial-gradient(ellipse at 50% 35%, var(--red-glow) 0%, var(--red) 45%, var(--red-deep) 100%);
  }
  .sparkle-top, .sparkle-bottom {
    position: absolute;
    left: 0; right: 0;
    pointer-events: none;
  }
  .sparkle-top {
    top: 0; height: 130px;
    background: linear-gradient(180deg, rgba(255,255,255,.16), transparent);
  }
  .sparkle-bottom {
    bottom: 0; height: 110px;
    background: linear-gradient(0deg, rgba(255,220,200,.18), transparent);
  }
  .title-swoosh {
    position: absolute;
    left: 0; top: 385px;
    width: 750px; height: 110px;
  }
  .logo {
    position: absolute;
    top: 40px; left: 0; right: 0;
    text-align: center;
    font-family: "Great Vibes", cursive;
    color: var(--white);
    font-weight: 400;
    line-height: .88;
  }
  .logo-line { display: block; }
  .logo-line--first { font-size: 200px; margin-left: -40px; }
  .logo-line--second { font-size: 190px; margin-top: -22px; }
  .title-kana {
    position: absolute;
    top: 462px; left: 0; right: 0;
    text-align: center;
    color: var(--white);
    font-weight: 700;
    font-size: 46px;
    letter-spacing: 4px;
    line-height: 1.3;
  }
  .author {
    position: absolute;
    top: 528px; left: 0; right: 0;
    text-align: center;
    color: var(--white);
    font-weight: 900;
    font-size: 76px;
    letter-spacing: 4px;
    line-height: 1.3;
  }
  .tagline {
    position: absolute;
    top: 728px; left: 0; right: 0;
    text-align: center;
    font-family: "Great Vibes", cursive;
    color: rgba(255,255,255,.9);
    font-size: 26px;
    letter-spacing: 1px;
  }

  /* ---------- green band ---------- */
  .band {
    position: absolute;
    left: 0; right: 0; bottom: 0;
    height: 410px;
    background: radial-gradient(ellipse at 50% 50%, var(--green) 0%, var(--green-deep) 100%);
    border-top: 5px solid var(--white);
  }
  .band-frost {
    position: absolute;
    inset: 0;
    background:
      linear-gradient(90deg, rgba(255,255,255,.3), transparent 12%, transparent 88%, rgba(255,255,255,.3)),
      linear-gradient(0deg, rgba(255,255,255,.3), transparent 14%, transparent 90%, rgba(255,255,255,.2));
  }
  .band-ribbon {
    position: absolute;
    left: 0; top: 0;
    width: 150px; height: 150px;
    background: linear-gradient(135deg, var(--gold-light) 0%, var(--gold) 40%, var(--gold-deep) 70%, transparent 71%);
  }
  .band-copy {
    position: absolute;
    inset: 0;
    text-align: center;
    font-weight: 900;
  }
  .copy-lifetime {
    position: absolute;
    top: 62px; left: 0; right: 0;
    color: var(--white);
    font-size: 62px;
    letter-spacing: 4px;
    line-height: 1.2;
  }
  .copy-concept {
    position: absolute;
    top: 146px; left: 0; right: 0;
    color: var(--cream);
    font-size: 48px;
    letter-spacing: 4px;
    line-height: 1.2;
  }
  .copy-textbook {
    position: absolute;
    top: 205px; left: 0; right: 0;
    font-family: "Shippori Mincho B1", serif;
    font-weight: 800;
    font-size: 132px;
    letter-spacing: 14px;
    line-height: 1.2;
    background: linear-gradient(180deg, var(--gold-light) 0%, var(--gold) 45%, var(--gold-deep) 100%);
    -webkit-background-clip: text;
    background-clip: text;
    color: transparent;
  }
</style>
</head>
<body>
<main class="cover">
  <section class="title-field">
    <div class="sparkle-top" role="img" aria-label="Soft glittering lights along the top edge"></div>
    <svg class="title-swoosh" viewBox="0 0 750 110" aria-hidden="true">
      <path d="M0 0 Q375 70 750 0 L750 35 Q375 110 0 35 Z" fill="#b00812" opacity=".55"/>
      <path d="M0 8 Q375 85 750 8" fill="none" stroke="#f35a5a" stroke-width="3" opacity=".6"/>
    </svg>
    <h1 class="logo">
      <span class="logo-line logo-line--first">Vellum</span>
      <span class="logo-line logo-line--second">Core</span>
    </h1>
    <p class="title-kana">ヴェラム・コア</p>
    <p class="author">岡崎 隆之介</p>
    <p class="tagline">Think about concept making.</p>
    <div class="sparkle-bottom" role="img" aria-label="Golden sparkles along the lower edge"></div>
  </section>

  <section class="band">
    <div class="band-frost" role="img" aria-label="Frosted snowflake border around the band"></div>
    <div class="band-ribbon" role="img" aria-label="Gold ribbon bow in the corner"></div>
    <div class="band-copy">
      <p class="copy-lifetime">一生、頼れる</p>
      <p class="copy-concept">アイデアの</p>
      <p class="copy-textbook">指南書</p>
    </div>
  </section>
</main>
</body>
</html>
```